Velumin clinic business card - double sided for young clinic

I require business cards for my aesthetic clinic specialising in the below treatments. I would like the cards to be modern as my clinic base are young 22-35 years old. I require my logo on it and would like the edges to be rounded.

I have an aesthetic clinic specialising in :
Velumin
Lip Enhancement
Chemical Peels
Facial Fillers
Non Surgical Face Lift

I would the cards to have the following information on them:
My logo - (in grey/silver)
address
Phone number
services

Colours :
White/grey/silver and red

a nice image on there, perhaps a set of lips as this is a main service i deliver

Company Name: HFA Address: 52 Harwell Lane, 4 Brimfold High Street, TN7 4QW Phone: 0207 948 2176 Website: www.helenfosburyaesthetics-example.co.uk

Target Market(s)

clinics 22-45 years old mainly female

Industry/Entity Type

Business

Contact Information for Business Card

as above

Requirements
Must have
• logo
• Address
• Email
• Phone number
• Services i offer
Nice to have
• images

```html
<!DOCTYPE html>
<html lang="en">
<head>
<meta charset="utf-8">
<title>HFA – Business Card</title>
<link rel="stylesheet" href="https://fonts.googleapis.com/css2?family=Alegreya:wght@400&family=Tinos:wght@400;700&family=Cormorant+Garamond:ital,wght@1,500&display=swap">
<style>
  :root {
    --stage: #ebe8e3;
    --card: #ffffff;
    --band: #8a8a8c;
    --swoosh: #bdbdc0;
    --brand-grey: #a3a3a6;
    --ink: #555555;
    --accent-red: #e0181b;
    --service-grey: #9c9ca0;
    --photo-light: #f4efec;
    --photo-mid: #e2d3cb;
  }
  * { margin: 0; padding: 0; box-sizing: border-box; }
  html, body { width: 1000px; height: 1200px; overflow: hidden; background: var(--stage); }
  .canvas { position: relative; width: 1000px; height: 1200px; }

  .card {
    position: absolute; left: 58px; width: 898px;
    background: var(--card); border-radius: 24px; overflow: hidden;
    box-shadow: 0 6px 18px rgba(0,0,0,.18);
  }
  .card--front { top: 57px; height: 519px; }
  .card--back { top: 620px; height: 530px; }

  .portrait {
    position: absolute; left: 0; top: 0; width: 380px; height: 400px;
    background: radial-gradient(ellipse at 35% 35%, var(--photo-mid) 0%, var(--photo-light) 55%, rgba(255,255,255,0) 80%);
  }

  .wave { position: absolute; left: 0; top: 0; width: 898px; height: 519px; }

  .brand { position: absolute; text-align: center; color: var(--brand-grey); font-family: "Alegreya", serif; font-weight: 400; }
  .brand__mark {
    display: flex; align-items: center; justify-content: center;
    width: 150px; height: 150px; margin: 0 auto; border: 3px solid var(--brand-grey); border-radius: 50%;
    font-size: 50px; letter-spacing: 3px;
  }
  .brand__name-top { font-size: 33px; letter-spacing: 4px; line-height: 1; margin-top: 22px; }
  .brand__name-main { font-size: 45px; letter-spacing: 4px; line-height: 1; margin-top: 4px; }
  .card--front .brand { left: 490px; top: 40px; width: 380px; }
  .card--back .brand { left: 250px; top: 50px; width: 400px; }

  .person { position: absolute; left: 64px; top: 312px; font-family: "Tinos", serif; font-weight: 700; }
  .person__name { color: var(--ink); font-size: 26px; }
  .person__title { color: var(--accent-red); font-size: 25px; margin-top: 2px; }

  .contact { position: absolute; right: 38px; top: 366px; text-align: right; color: #fff; font-family: "Tinos", serif; font-size: 20px; line-height: 28px; }
  .contact__phone { margin-top: 12px; }
  .website { position: absolute; left: 54px; top: 474px; color: #fff; font-family: "Tinos", serif; font-size: 20px; }

  .services-heading { position: absolute; left: 44px; top: 358px; width: 810px; display: flex; align-items: center; gap: 22px; }
  .services-heading__rule { flex: 1; height: 3px; background: var(--brand-grey); }
  .services-heading__text { font-family: "Cormorant Garamond", serif; font-style: italic; font-weight: 500; font-size: 34px; color: var(--service-grey); }

  .services { position: absolute; left: 0; top: 408px; width: 898px; text-align: center; font-family: "Tinos", serif; font-weight: 700; font-size: 21px; color: var(--service-grey); line-height: 33px; }
  .services__heart { display: inline-block; width: 16px; height: 14px; margin: 0 8px; vertical-align: -1px; }
</style>
</head>
<body>
<div class="canvas">

  <section class="card card--front">
    <div class="portrait" role="img" aria-label="Beauty photograph of a woman's face with a treatment syringe near the cheek"></div>
    <svg class="wave" viewBox="0 0 898 519" aria-hidden="true">
      <path d="M0,372 C140,430 270,455 420,408 C560,362 700,318 898,345 L898,352 C700,330 560,372 420,418 C270,468 140,448 0,392 Z" fill="var(--swoosh)"/>
      <path d="M0,402 C140,458 270,478 430,428 C580,380 720,335 898,372 L898,519 L0,519 Z" fill="var(--band)"/>
    </svg>

    <div class="brand">
      <div class="brand__mark">HFA</div>
      <div class="brand__name-top">HELEN FOSBURY</div>
      <div class="brand__name-main">AESTHETICS</div>
    </div>

    <div class="person">
      <div class="person__name">Your Name Here</div>
      <div class="person__title">title here</div>
    </div>

    <div class="contact">
      <div>52 Harwell Lane</div>
      <div>4 Brimfold High Street, TN7 4QW</div>
      <div class="contact__phone">Phone: 0207 948 2176</div>
      <div>Email: mail@youremail.co.uk</div>
    </div>

    <div class="website">www.helenfosburyaesthetics-example.co.uk</div>
  </section>

  <section class="card card--back">
    <div class="brand">
      <div class="brand__mark">HFA</div>
      <div class="brand__name-top">HELEN FOSBURY</div>
      <div class="brand__name-main">AESTHETICS</div>
    </div>

    <div class="services-heading">
      <span class="services-heading__rule"></span>
      <span class="services-heading__text">Specialising in</span>
      <span class="services-heading__rule"></span>
    </div>

    <div class="services">
      <div>Velumin<svg class="services__heart" viewBox="0 0 16 14"><path d="M8,14 L1.5,7.5 A4,4 0 0 1 8,2.5 A4,4 0 0 1 14.5,7.5 Z" fill="currentColor"/></svg>Lip Enhancement<svg class="services__heart" viewBox="0 0 16 14"><path d="M8,14 L1.5,7.5 A4,4 0 0 1 8,2.5 A4,4 0 0 1 14.5,7.5 Z" fill="currentColor"/></svg>Chemical Peels</div>
      <div>Facial Fillers<svg class="services__heart" viewBox="0 0 16 14"><path d="M8,14 L1.5,7.5 A4,4 0 0 1 8,2.5 A4,4 0 0 1 14.5,7.5 Z" fill="currentColor"/></svg>Non Surgical Face Lift</div>
    </div>
  </section>

</div>
</body>
</html>
```